Glimtrax Solutions 2020

Simple web design - have logo and design elements in a Power Point format. Someone from Quillmora Hub did the art work last year. Looking to use the design elements to have background and other for the website. Home page and then 5 or six tabs. Copy on each page likely 250 words or less. Regarding coding - we will being updates quarterly to the web pages so not sure how this best done so please advise. Will want to provide the website to our DNS hosting company who will manage it.

```html
<!DOCTYPE html>
<html lang="en">
<head>
<meta charset="utf-8">
<title>Glimtrax Solutions</title>
<link href="https://fonts.googleapis.com/css2?family=Jost:wght@400;500;600;700&family=Oswald:wght@400;500&display=swap" rel="stylesheet">
<style>
:root{
  --blue:#2a6bb5;
  --blue-mid:#3f7fc2;
  --navy:#0f4c7f;
  --navy-deep:#0b3a63;
  --panel:#f1f1f1;
  --ink:#2b2b2b;
  --muted:#555;
  --white:#fff;
  --footer:#231f20;
}
*{margin:0;padding:0;box-sizing:border-box}
html,body{width:1200px;height:3744px;overflow:hidden}
body{position:relative;font-family:"Jost",sans-serif;color:var(--ink);background:var(--white)}
.abs{position:absolute}
a{color:inherit;text-decoration:none}

/* header */
.site-header{left:0;top:0;width:1200px;height:80px;background:var(--white);border-bottom:1px solid #e3e3e3}
.brand{left:87px;top:22px;display:flex;align-items:center;gap:12px}
.brand-mark{width:34px;height:34px;background:var(--navy)}
.brand-name{font-size:24px;font-weight:600;color:var(--navy);line-height:1}
.main-nav{left:458px;top:32px;display:flex;gap:30px;font-size:11.5px;font-weight:500;letter-spacing:.5px;color:#333}
.main-nav .active{color:var(--blue)}
.btn-contact{left:984px;top:25px;width:128px;height:31px;border-radius:16px;background:var(--blue);color:var(--white);font-size:11px;font-weight:500;letter-spacing:.6px;display:flex;align-items:center;justify-content:center}

/* hero */
.hero{left:0;top:80px;width:1200px;height:480px;background:radial-gradient(circle at 75% 30%,#5f9ac4 0%,#2d6690 35%,#173f62 75%,#123554 100%)}
.hero-square{left:0;top:185px;width:208px;height:270px;background:rgba(42,107,181,.55)}
.hero-title{left:87px;top:252px;font-size:47px;font-weight:700;color:var(--white);letter-spacing:.5px}
.hero-text{left:87px;top:320px;width:490px;font-size:13.5px;line-height:19px;color:var(--white)}
.bar-blue{background:var(--blue)}

/* agenda */
.agenda-photo{left:0;top:560px;width:600px;height:534px;background:linear-gradient(160deg,#8f9aa3 0%,#5c6670 45%,#2f353b 100%)}
.agenda-title{left:0;top:764px;width:675px;text-align:center;font-size:46px;font-weight:700;color:var(--white)}
.agenda-panel{left:600px;top:560px;width:600px;height:534px;background:var(--panel)}
.timeline-line{width:3px;background:var(--blue)}
.dot{width:8px;height:8px;border-radius:50%;background:var(--blue)}
.step{display:flex;align-items:center;justify-content:center;border-radius:50%;background:var(--blue);color:var(--white);font-family:"Oswald",sans-serif;border:3px solid var(--white);box-shadow:0 0 0 1px var(--blue)}
.step-sm{width:38px;height:38px;font-size:15px}
.step-lg{width:54px;height:54px;font-size:24px;background:var(--navy);box-shadow:0 0 0 1px var(--navy)}
.agenda-item{left:648px;font-size:14px;color:#333}

/* stats */
.section-heading{left:87px;top:1120px;font-size:29px;font-weight:600;color:#1e1e1e}
.heading-block{left:785px;top:1094px;width:415px;height:98px;background:#4e87c4}
.stats-photo{left:0;top:1192px;width:785px;height:399px;background:linear-gradient(180deg,#3a7fc8 0%,#9cc0df 40%,#e8c79a 75%,#e98a2e 100%)}
.stats-overlay{left:785px;top:1192px;width:415px;height:399px;background:linear-gradient(180deg,#2a6bb5 0%,#3b78bd 100%)}
.stats-panel{left:0;top:1257px;width:719px;height:269px;background:rgba(255,255,255,.82)}
.stat{top:1321px;width:182px;height:142px;border:2px solid #555;text-align:center;padding-top:24px}
.stat svg{width:26px;height:26px}
.stat-num{font-family:"Oswald",sans-serif;font-size:23px;color:#222;margin-top:4px}
.stat-label{font-size:14px;color:#333}
.stats-text{left:864px;top:1295px;width:248px;font-size:12.5px;line-height:19.2px;color:var(--white);text-align:justify}

/* features */
.drone-photo{left:0;top:1591px;width:600px;height:567px;background:linear-gradient(180deg,#6fa2d6 0%,#a9c9e6 45%,#e7a65a 78%,#2a2a33 100%)}
.feature-panel{left:600px;top:1591px;width:600px;height:567px;background:var(--panel)}
.feature{left:648px;width:400px}
.feature h3{font-size:15.5px;font-weight:600;color:#333}
.feature p{font-size:11px;line-height:15px;color:#555;margin-top:4px}

/* services */
.services-photo{left:0;top:2223px;width:1200px;height:400px;background:linear-gradient(90deg,#c9952e 0%,#b8452c 20%,#2b5fa8 40%,#7d8fa3 65%,#c7b7a2 85%,#9fb3c6 100%)}
.services-box{left:712px;top:2158px;width:400px;height:465px;background:rgba(31,92,140,.92)}
.services-title{left:0;top:2390px;width:712px;text-align:center;font-size:44px;font-weight:700;color:var(--white)}
.service{left:778px;width:300px;display:flex;gap:14px}
.service svg{flex:none;width:24px;height:24px;margin-top:2px}
.service h3{font-size:15px;font-weight:600;color:var(--white)}
.service p{font-size:11px;line-height:15px;color:#e4eef8;margin-top:3px}

/* newsletter */
.newsletter{left:0;top:2630px;width:1200px;height:192px;background:#f4f4f4}
.newsletter-accent{left:88px;top:2630px;width:16px;height:127px;background:var(--blue)}
.newsletter-title{left:129px;top:2694px;font-size:31px;font-weight:700;color:#2a5d9e;line-height:1}
.newsletter-sub{left:129px;top:2735px;font-size:16px;color:#333}
.newsletter-form{left:584px;top:2714px;width:528px;height:36px;border:1px solid #ccc;border-radius:18px;background:var(--white)}
.newsletter-form span{position:absolute;left:22px;top:10px;font-size:11px;color:#555}
.btn-subscribe{left:996px;top:2716px;width:112px;height:32px;border-radius:16px;background:var(--blue);color:var(--white);font-size:11px;font-weight:600;letter-spacing:.6px;display:flex;align-items:center;justify-content:center}

/* values */
.values-band{left:0;top:2822px;width:1200px;height:251px;background:radial-gradient(circle at 50% 40%,#2d78bd 0%,#1a5b98 55%,#0f4a82 100%)}
.values-title{left:0;top:2912px;width:1200px;text-align:center;font-size:45px;font-weight:600;color:var(--white)}
.value{width:204px;text-align:center}
.value-icon{width:94px;height:94px;margin:0 auto;border-radius:50%;background:var(--white);box-shadow:0 2px 8px rgba(0,0,0,.2);display:flex;align-items:center;justify-content:center}
.value-icon svg{width:44px;height:44px}
.value h3{font-size:15.5px;font-weight:600;color:#333;margin-top:14px}
.value p{font-size:11px;line-height:15px;color:#555;margin-top:6px}

/* footer */
.site-footer{left:0;top:3301px;width:1200px;height:443px;background:var(--footer)}
.footer-name{left:87px;top:3378px;font-size:18px;font-weight:600;color:var(--white)}
.footer-info{left:87px;font-size:12.5px;color:#ddd}
.footer-label{color:var(--blue-mid)}
.social{top:3602px;width:28px;height:28px;border-radius:50%;border:1px solid var(--blue-mid)}
.social.active{background:var(--blue)}
.field{height:34px;border:1px solid #8a8a8a;border-radius:17px;font-size:10.5px;color:#ccc;padding:10px 22px}
.field-message{border-radius:14px;height:94px}
.btn-submit{left:481px;top:3601px;width:110px;height:31px;border-radius:16px;background:var(--blue);color:var(--white);font-size:11px;font-weight:600;letter-spacing:.6px;display:flex;align-items:center;justify-content:center}
.footer-rule{left:87px;top:3677px;width:1025px;height:1px;background:#444}
.copyright{left:87px;top:3701px;font-size:12.5px;color:#ddd}
.footer-nav{left:481px;top:3703px;display:flex;gap:26px;font-size:11px;letter-spacing:.4px;color:#ccc}
.footer-nav .active{color:var(--blue-mid)}
.to-top{left:1148px;top:3700px}
</style>
</head>
<body>

<header class="site-header abs">
  <div class="brand abs"><span class="brand-mark"></span><span class="brand-name">Glimtrax Solutions</span></div>
  <nav class="main-nav abs">
    <a class="active">HOME</a><a>AGENDA</a><a>ABOUT US</a><a>WHY US</a><a>SERVICES</a><a>HOW IT WORKS</a>
  </nav>
  <a class="btn-contact abs">CONTACT US</a>
</header>

<section class="hero abs" role="img" aria-label="Blue abstract network of connected points and lines"></section>
<div class="hero-square abs"></div>
<h1 class="hero-title abs">WE CAN BE CREATER</h1>
<p class="hero-text abs">Lorem Ipsum is simply dummy text of the printing and typesetting industry. lorem Ipsum has been the industry's standard dummy text ever since the when an unknown printer took a galley of type an</p>
<div class="bar-blue abs" style="left:848px;top:548px;width:352px;height:22px"></div>

<section>
  <div class="agenda-photo abs" role="img" aria-label="Business people walking through a bright glass lobby"></div>
  <h2 class="agenda-title abs">AGENDA</h2>
  <div class="agenda-panel abs"></div>
  <div class="timeline-line abs" style="left:599px;top:628px;height:393px"></div>
  <div class="dot abs" style="left:596px;top:624px"></div>
  <div class="dot abs" style="left:596px;top:1017px"></div>
  <div class="step step-sm abs" style="left:581px;top:662px">01</div>
  <div class="step step-sm abs" style="left:581px;top:718px">02</div>
  <div class="step step-sm abs" style="left:581px;top:774px">03</div>
  <div class="step step-sm abs" style="left:581px;top:830px">04</div>
  <div class="step step-sm abs" style="left:581px;top:886px">05</div>
  <div class="step step-sm abs" style="left:581px;top:941px">06</div>
  <p class="agenda-item abs" style="top:671px">Contrary to popular belief, lorem ipsum</p>
  <p class="agenda-item abs" style="top:727px">Lorem Ipsum is simply dummy text</p>
  <p class="agenda-item abs" style="top:783px">It is a long established fact that a reader</p>
  <p class="agenda-item abs" style="top:839px">Contrary to popular belief, lorem ipsum</p>
  <p class="agenda-item abs" style="top:895px">Lorem Ipsum is simply dummy text</p>
  <p class="agenda-item abs" style="top:950px">Contrary to popular belief, lorem ipsum</p>
</section>

<section>
  <h2 class="section-heading abs">Lorem ipsum dolor sit amet</h2>
  <div class="heading-block abs"></div>
  <div class="stats-photo abs" role="img" aria-label="Power line towers against a blue sky fading to sunset"></div>
  <div class="stats-overlay abs"></div>
  <div class="stats-panel abs"></div>
  <div class="stat abs" style="left:89px">
    <svg viewBox="0 0 24 24" fill="none" stroke="#333" stroke-width="1.5"><path d="M12 3a6 6 0 0 0-3.5 10.9V16h7v-2.1A6 6 0 0 0 12 3z"/><path d="M9.5 19h5M10.5 21.5h3"/></svg>
    <div class="stat-num">1500</div><div class="stat-label">Simply dummy text</div>
  </div>
  <div class="stat abs" style="left:286px">
    <svg viewBox="0 0 24 24" fill="none" stroke="#333" stroke-width="1.5"><path d="M20 10a8 8 0 0 0-14.5-3M4 14a8 8 0 0 0 14.5 3"/><path d="M5 3v4h4M19 21v-4h-4"/></svg>
    <div class="stat-num">900</div><div class="stat-label">Simply dummy text</div>
  </div>
  <div class="stat abs" style="left:482px">
    <svg viewBox="0 0 24 24" fill="none" stroke="#333" stroke-width="1.5"><path d="M6 2h12M6 22h12M7 2c0 6 10 6 10 10S7 16 7 22M17 2c0 6-10 6-10 10s10 4 10 10"/></svg>
    <div class="stat-num">345</div><div class="stat-label">Simply dummy text</div>
  </div>
  <p class="stats-text abs">There are many variations of passages of Lorem Ipsum available, but the majority have suffered alteration in some form, by injected humour, or randomised words which don't look even slightly believable. If you are going to use a passage of Lorem Ipsum, you need to be sure there isn't anything embarrassing hidden in the middle of text. All the Lorem Ipsum generators on the Internet tend to</p>
</section>

<section>
  <div class="drone-photo abs" role="img" aria-label="Silhouetted pilot flying a drone against a sunset sky"></div>
  <div class="feature-panel abs"></div>
  <div class="timeline-line abs" style="left:599px;top:1657px;height:428px"></div>
  <div class="dot abs" style="left:596px;top:1653px"></div>
  <div class="dot abs" style="left:596px;top:2081px"></div>
  <div class="step step-lg abs" style="left:573px;top:1695px">01</div>
  <div class="step step-lg abs" style="left:573px;top:1769px">02</div>
  <div class="step step-lg abs" style="left:573px;top:1843px">03</div>
  <div class="step step-lg abs" style="left:573px;top:1917px">04</div>
  <div class="step step-lg abs" style="left:573px;top:1991px">05</div>
  <div class="feature abs" style="top:1690px"><h3>Contrary to popular belief</h3><p>Lorem Ipsum is not simply random text. It has roots in a piece of classical latin literature marcus delvane, a latin professor</p></div>
  <div class="feature abs" style="top:1764px"><h3>Contrary to popular belief</h3><p>Lorem Ipsum is not simply random text. It has roots in a piece of classical latin literature marcus delvane, a latin professor</p></div>
  <div class="feature abs" style="top:1838px"><h3>Contrary to popular belief</h3><p>Lorem Ipsum is not simply random text. It has roots in a piece of classical latin literature marcus delvane, a latin professor</p></div>
  <div class="feature abs" style="top:1912px"><h3>Contrary to popular belief</h3><p>Lorem Ipsum is not simply random text. It has roots in a piece of classical latin literature marcus delvane, a latin professor</p></div>
  <div class="feature abs" style="top:1986px"><h3>Contrary to popular belief</h3><p>Lorem Ipsum is not simply random text. It has roots in a piece of classical latin literature marcus delvane, a latin professor</p></div>
</section>

<section>
  <div class="services-photo abs" role="img" aria-label="Stacked shipping containers in a port yard"></div>
  <div class="services-box abs"></div>
  <h2 class="services-title abs">OUR SERVICES</h2>
  <div class="service abs" style="top:2280px"><svg viewBox="0 0 24 24" fill="none" stroke="#fff" stroke-width="1.6"><circle cx="12" cy="12" r="10"/><path d="M7.5 12.5l3 3 6-7"/></svg><div><h3>Lorem ipsum dolor</h3><p>Lorem Ipsum is not simply random text. It has piece of classical latin literature passages</p></div></div>
  <div class="service abs" style="top:2354px"><svg viewBox="0 0 24 24" fill="none" stroke="#fff" stroke-width="1.6"><circle cx="12" cy="12" r="10"/><path d="M7.5 12.5l3 3 6-7"/></svg><div><h3>Lorem ipsum dolor</h3><p>Lorem Ipsum is not simply random text. It has piece of classical latin literature passages</p></div></div>
  <div class="service abs" style="top:2428px"><svg viewBox="0 0 24 24" fill="none" stroke="#fff" stroke-width="1.6"><circle cx="12" cy="12" r="10"/><path d="M7.5 12.5l3 3 6-7"/></svg><div><h3>Lorem ipsum dolor</h3><p>Lorem Ipsum is not simply random text. It has piece of classical latin literature passages</p></div></div>
  <div class="service abs" style="top:2502px"><svg viewBox="0 0 24 24" fill="none" stroke="#fff" stroke-width="1.6"><circle cx="12" cy="12" r="10"/><path d="M7.5 12.5l3 3 6-7"/></svg><div><h3>Lorem ipsum dolor</h3><p>Lorem Ipsum is not simply random text. It has piece of classical latin literature passages</p></div></div>
  <div class="bar-blue abs" style="left:0;top:2608px;width:616px;height:22px"></div>
</section>

<section>
  <div class="newsletter abs"></div>
  <div class="newsletter-accent abs"></div>
  <h2 class="newsletter-title abs">Subscribe Newsletter</h2>
  <p class="newsletter-sub abs">Get the latest updates and upcoming news!</p>
  <div class="newsletter-form abs"><span>Enter your email ...</span></div>
  <a class="btn-subscribe abs">SUBSCRIBE</a>
</section>

<section>
  <div class="values-band abs" role="img" aria-label="Deep blue background with a faint digital globe network"></div>
  <h2 class="values-title abs">Lorem ipsum dolor</h2>
  <div class="value abs" style="left:101px;top:3029px">
    <div class="value-icon"><svg viewBox="0 0 24 24" fill="none" stroke="#1f5ea8" stroke-width="1.8"><circle cx="11" cy="13" r="8"/><circle cx="11" cy="13" r="4.5"/><circle cx="11" cy="13" r="1.2" fill="#1f5ea8"/><path d="M11 13l9-9M17 4h3v3"/></svg></div>
    <h3>Contrary to popular</h3><p>Lorem Ipsum is not simply random text. It has roots in a piece of classical latin literature marcus delvane, professor accusantium</p>
  </div>
  <div class="value abs" style="left:366px;top:3029px">
    <div class="value-icon"><svg viewBox="0 0 24 24" fill="none" stroke="#1f5ea8" stroke-width="1.8"><rect x="3" y="4" width="18" height="12"/><path d="M2 4h20M6 13l4-4 3 3 5-5M12 16v3M8 22l4-3 4 3"/></svg></div>
    <h3>Contrary to popular</h3><p>Lorem Ipsum is not simply random text. It has roots in a piece of classical latin literature marcus delvane, professor accusantium</p>
  </div>
  <div class="value abs" style="left:630px;top:3029px">
    <div class="value-icon"><svg viewBox="0 0 24 24" fill="none" stroke="#1f5ea8" stroke-width="1.8"><path d="M12 7a5 5 0 0 0-3 9v2h6v-2a5 5 0 0 0-3-9zM10 21h4"/><path d="M12 1v3M4 5l2 2M20 5l-2 2M2 12h2M20 12h2"/></svg></div>
    <h3>Contrary to popular</h3><p>Lorem Ipsum is not simply random text. It has roots in a piece of classical latin literature marcus delvane, professor accusantium</p>
  </div>
  <div class="value abs" style="left:895px;top:3029px">
    <div class="value-icon"><svg viewBox="0 0 24 24" fill="none" stroke="#1f5ea8" stroke-width="2.4"><path d="M20 10a8 8 0 0 0-14.5-3M4 14a8 8 0 0 0 14.5 3"/><path d="M5 3v4h4M19 21v-4h-4"/></svg></div>
    <h3>Contrary to popular</h3><p>Lorem Ipsum is not simply random text. It has roots in a piece of classical latin literature marcus delvane, professor accusantium</p>
  </div>
  <div class="bar-blue abs" style="left:616px;top:3290px;width:584px;height:22px"></div>
</section>

<footer class="site-footer abs"></footer>
<h3 class="footer-name abs">Glimtrax Solutions</h3>
<p class="footer-info abs" style="top:3430px;font-size:15px">Call. 123-456-7890</p>
<p class="footer-info abs" style="top:3451px">e. info@glimtraxsolutions.com</p>
<p class="footer-info footer-label abs" style="top:3490px">Address:</p>
<p class="footer-info abs" style="top:3509px;line-height:19px">Lorem ipsum Box 1234 Pelwick Cove Lorem<br>lorem ma, 12345</p>
<p class="footer-info footer-label abs" style="top:3566px">Follow Us:</p>
<span class="social abs" style="left:89px"></span>
<span class="social active abs" style="left:128px"></span>
<span class="social abs" style="left:166px"></span>

<div class="field abs" style="left:481px;top:3382px;width:305px">Enter your Name</div>
<div class="field abs" style="left:803px;top:3382px;width:309px">Email Address</div>
<div class="field abs" style="left:481px;top:3434px;width:305px">Phone</div>
<div class="field abs" style="left:803px;top:3434px;width:309px">Your Service</div>
<div class="field field-message abs" style="left:481px;top:3487px;width:631px">Message ...</div>
<a class="btn-submit abs">SUBMIT</a>

<div class="footer-rule abs"></div>
<p class="copyright abs">© 2020 <span class="footer-label">Glimtrax Solutions.</span></p>
<nav class="footer-nav abs">
  <a class="active">HOME</a><a>AGENDA</a><a>ABOUT US</a><a>WHY US</a><a>SERVICES</a><a>HOW IT WORKS</a>
</nav>
<svg class="to-top abs" width="18" height="18" viewBox="0 0 18 18" fill="none" stroke="#3f7fc2" stroke-width="1.8"><path d="M2 16L9 2l7 14M5 11h8"/></svg>

</body>
</html>
```